Torvane PT Business Card

I need the card to be bright/bold colours to stand out amongst others.
It needs to have my company logo.
I was not interested in pictures etc just a layout that attracts attention.

I have attached my old design which is very plain. I also needed change the contact details. And my description changed to Personal Trainer
Phone 0427391058
Facebook Torvane PT
No email address please, no street address.
And only Torvane PT (Please remove anything to do with Torvane Supplements)

```html
<!DOCTYPE html>
<html lang="en">
<head>
<meta charset="utf-8">
<title>Torvane PT Business Card</title>
<link rel="stylesheet" href="https://fonts.googleapis.com/css2?family=Montserrat:wght@600;700;800&family=Lato:wght@400;700&display=swap">
<style>
  :root {
    --page-bg: #2e2e2e;
    --card-white: #f7f7f7;
    --brand-blue: #1b7ec0;
    --brand-yellow: #f2cb12;
    --ink-dark: #2a2a2a;
    --ink-grey: #444444;
  }
  html, body {
    margin: 0;
    width: 1200px;
    height: 997px;
    overflow: hidden;
    background: var(--page-bg);
  }
  .business-card {
    position: absolute;
    left: 150px;
    top: 241px;
    width: 900px;
    height: 514px;
    background: var(--card-white);
    overflow: hidden;
    font-family: "Lato", sans-serif;
  }
  .brand-name {
    position: absolute;
    left: 0;
    right: 0;
    top: 62px;
    margin: 0;
    text-align: center;
    font-family: "Montserrat", sans-serif;
    font-weight: 800;
    font-size: 64px;
    letter-spacing: 1px;
    color: var(--brand-blue);
    line-height: 1;
  }
  .brand-rule {
    position: absolute;
    left: 250px;
    width: 420px;
    top: 150px;
    height: 2px;
    background: var(--brand-blue);
  }
  .company-name {
    position: absolute;
    right: 64px;
    top: 284px;
    font-weight: 700;
    font-size: 19px;
    line-height: 1;
    color: var(--brand-blue);
  }
  .person {
    position: absolute;
    left: 58px;
    top: 312px;
  }
  .person-name {
    margin: 0;
    font-family: "Montserrat", sans-serif;
    font-weight: 700;
    font-size: 26px;
    color: var(--brand-blue);
    line-height: 1;
  }
  .person-role {
    margin: 4px 0 0;
    font-family: "Montserrat", sans-serif;
    font-weight: 700;
    font-size: 15px;
    color: var(--ink-dark);
  }
  .name-rule {
    position: absolute;
    left: 278px;
    right: 64px;
    top: 322px;
    height: 2px;
    background: var(--brand-blue);
  }
  .contact-list {
    position: absolute;
    left: 58px;
    top: 382px;
    margin: 0;
    padding: 0;
    list-style: none;
  }
  .contact-item {
    display: flex;
    align-items: center;
    gap: 14px;
    height: 30px;
    font-family: "Montserrat", sans-serif;
    font-weight: 600;
    font-size: 20px;
    letter-spacing: 1px;
    color: var(--ink-grey);
  }
  .contact-icon {
    width: 18px;
    height: 18px;
    flex: none;
  }
  .footer-bands {
    position: absolute;
    left: 0;
    bottom: 0;
    width: 900px;
    height: 120px;
  }
</style>
</head>
<body>
  <main class="business-card">
    <h1 class="brand-name">TORVANE PT</h1>
    <div class="brand-rule"></div>

    <div class="company-name">TORVANE PT PVT LTD.</div>

    <div class="person">
      <h2 class="person-name">SAM HARLOW</h2>
      <p class="person-role">Personal Trainer</p>
    </div>
    <div class="name-rule"></div>

    <ul class="contact-list">
      <li class="contact-item">
        <svg class="contact-icon" viewBox="0 0 18 18" aria-hidden="true">
          <circle cx="9" cy="9" r="9" fill="var(--brand-blue)"/>
          <path d="M6 4.5c.5-.3 1-.2 1.3.3l.8 1.5c.2.4.1.8-.2 1.1l-.6.5c.4 1 1.2 1.8 2.2 2.2l.5-.6c.3-.3.7-.4 1.1-.2l1.5.8c.5.3.6.8.3 1.3l-.5.7c-.5.6-1.3.8-2 .5-2.4-1-4.2-2.8-5.2-5.2-.3-.7-.1-1.5.5-2z" fill="#fff"/>
        </svg>
        <span>0427391058</span>
      </li>
      <li class="contact-item">
        <svg class="contact-icon" viewBox="0 0 18 18" aria-hidden="true">
          <circle cx="9" cy="9" r="9" fill="var(--brand-blue)"/>
        </svg>
        <span>Torvane PT</span>
      </li>
    </ul>

    <svg class="footer-bands" viewBox="0 0 900 120" aria-hidden="true">
      <path d="M0 104 H490 C535 104 540 40 600 40 H900 V120 H0 Z" fill="var(--brand-blue)"/>
      <path d="M0 82 H470 Q500 82 514 70 Q508 94 470 94 H0 Z" fill="var(--brand-yellow)"/>
    </svg>
  </main>
</body>
</html>
```